Larkspur Vale Management

I need a professional website. My current website is larkspurvalemanagement.com and I hate it. It was created with some AI tool very quickly because I needed a site up and running with no advanced notice. I’m open to all designs .. I trust you, the professionals will deliver the results I’m anxiously awaiting! :)

```html
<!DOCTYPE html>
<html lang="en">
<head>
<meta charset="utf-8">
<title>Larkspur Vale Management</title>
<link href="https://fonts.googleapis.com/css2?family=Barlow:ital,wght@0,400;0,500;0,600;1,400&family=Barlow+Condensed:wght@600;700;800&display=swap" rel="stylesheet">
<style>
:root{
  --navy:#1c3a6f;
  --navy-deep:#13204a;
  --red:#c8262c;
  --ink:#13204a;
  --muted:#6b7385;
  --line:#dfe3ea;
  --paper:#f4f6fa;
  --white:#ffffff;
}
*{box-sizing:border-box;margin:0;padding:0}
html,body{width:1200px;height:4051px;overflow:hidden}
body{font-family:"Barlow",sans-serif;color:var(--ink);background:var(--white)}
.head{font-family:"Barlow Condensed",sans-serif;font-weight:800;text-transform:uppercase;letter-spacing:-.5px;line-height:1}
.eyebrow{font-family:"Barlow Condensed",sans-serif;font-weight:700;font-size:11px;letter-spacing:1.6px;color:var(--red);text-transform:uppercase}
.rule{width:54px;height:3px;background:var(--red)}
.btn{display:inline-flex;align-items:center;justify-content:center;gap:8px;font-family:"Barlow Condensed",sans-serif;font-weight:700;font-size:12px;letter-spacing:1.4px;text-transform:uppercase;text-decoration:none}
.btn-red{background:var(--red);color:var(--white)}
.btn-ghost{border:2px solid rgba(255,255,255,.7);color:var(--white)}
.section{position:relative;width:1200px}
.abs{position:absolute}

/* nav */
.nav{height:63px;background:var(--navy);display:flex;align-items:center;padding:0 80px;position:relative;z-index:2}
.brand{font-family:"Barlow Condensed",sans-serif;font-weight:800;font-size:17px;color:var(--white);text-transform:uppercase;display:flex;align-items:center;gap:8px}
.brand i{width:12px;height:12px;background:var(--red);display:block}
.nav-links{margin-left:auto;display:flex;gap:28px;align-items:center}
.nav-links a{font-family:"Barlow Condensed",sans-serif;font-weight:600;font-size:13px;letter-spacing:1.2px;color:var(--white);text-decoration:none}
.nav-links .btn{padding:10px 18px;font-size:13px}

/* hero */
.hero{height:684px;overflow:hidden}
.hero-photo{position:absolute;inset:0;background:linear-gradient(100deg,#23407a 0%,#2d4a80 40%,#566a8e 65%,#4a5c7a 80%,#3f5a4a 100%)}
.hero-shade{position:absolute;inset:0;background:linear-gradient(180deg,rgba(28,58,111,.35) 0%,rgba(28,58,111,.25) 70%,rgba(255,255,255,1) 100%)}
.hero .tag{left:80px;top:97px;background:rgba(200,38,44,.35);padding:5px 12px;color:#f2c7c9;display:flex;align-items:center;gap:7px}
.hero .tag::before{content:"";width:6px;height:6px;border-radius:50%;background:var(--red)}
.hero h1{left:80px;top:148px;font-size:64px;color:var(--white)}
.hero h1 span{color:var(--red);display:block}
.hero .lede{left:80px;top:303px;width:490px;font-size:14.5px;line-height:25px;color:#dfe6f2}
.hero .ctas{left:80px;top:410px;display:flex;gap:16px}
.hero .ctas .btn{height:52px;padding:0 28px}
.stats{left:80px;top:510px;display:flex;gap:34px}
.stat b{display:block;font-family:"Barlow Condensed",sans-serif;font-weight:800;font-size:32px;color:var(--white);font-style:italic}
.stat small{font-size:9.5px;letter-spacing:1.2px;color:#d4dbe8;text-transform:uppercase}

/* services */
.services{height:716px;background:var(--paper);text-align:center}
.services .eyebrow{position:absolute;top:98px;width:100%}
.center-title{position:absolute;width:100%;font-size:40px}
.services .rule{position:absolute;left:573px;top:178px}
.services .intro{position:absolute;top:195px;width:100%;font-size:13.5px;line-height:21px;color:var(--muted)}
.plans{position:absolute;left:80px;top:291px;display:flex;gap:21px}
.plan{width:245px;height:342px;background:var(--white);border:1px solid var(--line);padding:28px 28px 0;text-align:left;position:relative}
.plan .ico{width:42px;height:42px;background:#eef1f7;display:flex;align-items:center;justify-content:center}
.plan .price{margin-top:18px;font-family:"Barlow Condensed",sans-serif;font-weight:800;font-size:30px;color:var(--red)}
.plan .price small{font-family:"Barlow",sans-serif;font-weight:400;font-size:12px;color:var(--muted)}
.plan h3{font-family:"Barlow Condensed",sans-serif;font-weight:700;font-size:17px;margin-top:2px}
.plan p{margin-top:16px;font-size:11.5px;line-height:19.5px;color:var(--muted)}
.plan .btn{position:absolute;left:28px;right:28px;bottom:28px;height:36px;border:1px solid #b9c0cc;color:var(--ink);font-size:10px}
.plan.featured{background:var(--navy);border-color:var(--navy);box-shadow:0 14px 30px rgba(19,32,74,.25)}
.plan.featured .ico{background:rgba(255,255,255,.12)}
.plan.featured .price,.plan.featured h3{color:var(--white)}
.plan.featured .price small,.plan.featured p{color:#c9d3e6}
.plan.featured .btn{background:var(--red);border-color:var(--red);color:var(--white)}
.badge{position:absolute;top:-10px;left:74px;background:var(--red);color:var(--white);font-family:"Barlow Condensed",sans-serif;font-weight:700;font-size:9.5px;letter-spacing:1px;padding:3px 12px}

/* why */
.why{height:718px;background:var(--navy);overflow:hidden;color:var(--white)}
.ring{position:absolute;border-radius:50%;border:60px solid rgba(255,255,255,.04)}
.why .eyebrow{left:80px;top:94px}
.why h2{left:80px;top:116px;font-size:40px;color:var(--white)}
.why .rule{position:absolute;left:80px;top:219px}
.why .body{left:80px;top:250px;width:495px;font-size:13.5px;line-height:22.5px;color:#c9d3e6}
.checks{left:80px;top:374px;list-style:none}
.checks li{display:flex;align-items:center;gap:12px;height:27.7px;font-size:12px;color:#e4e9f3}
.why .btn{left:80px;top:590px;height:44px;padding:0 28px}
.why-photo{left:627px;top:178px;width:491px;height:364px;background:linear-gradient(160deg,#5f8a4e 0%,#b59f82 45%,#8b7865 70%,#6b6f73 100%);box-shadow:10px 12px 0 -2px rgba(200,38,44,.0),0 0 0 1px rgba(200,38,44,.5)}
.frame{left:637px;top:188px;width:494px;height:366px;border:1px solid rgba(200,38,44,.55)}
.occ{left:648px;top:450px;width:187px;height:72px;background:var(--red);padding:16px 18px}
.occ b{display:block;font-family:"Barlow Condensed",sans-serif;font-weight:800;font-size:24px;line-height:1}
.occ small{font-size:9.5px;letter-spacing:1.2px;text-transform:uppercase}

/* testimonials */
.stories{height:576px;background:var(--paper);text-align:center}
.stories .eyebrow{position:absolute;top:95px;width:100%}
.stories .rule{position:absolute;left:573px;top:172px}
.quotes{position:absolute;left:80px;top:232px;display:flex;gap:21px}
.quote{width:332px;height:260px;background:var(--white);border:1px solid var(--line);padding:28px;text-align:left;position:relative}
.stars{display:flex;gap:4px}
.quote p{margin-top:18px;font-size:11.5px;line-height:19.5px;font-style:italic;color:var(--muted)}
.quote .who{position:absolute;left:28px;right:28px;bottom:26px;border-top:1px solid var(--line);padding-top:22px}
.who b{display:block;font-family:"Barlow Condensed",sans-serif;font-weight:700;font-size:13px}
.who small{font-size:10px;letter-spacing:1px;color:var(--muted)}

/* cta band */
.cta{height:278px;background:var(--navy-deep);text-align:center;color:var(--white)}
.cta h2{position:absolute;top:60px;width:100%;font-size:34px}
.cta p{position:absolute;top:110px;width:100%;font-size:13.5px;line-height:21px;color:#c2cbdd}
.cta .row{position:absolute;top:175px;width:100%;display:flex;justify-content:center;gap:14px}
.cta .btn{height:47px;padding:0 34px;font-size:11px}
.cta .btn-ghost{border-width:1px;border-color:rgba(255,255,255,.5)}

/* contact */
.contact{height:650px;background:var(--white)}
.contact .eyebrow{left:80px;top:87px}
.contact h2{left:80px;top:112px;font-size:40px}
.contact .rule{position:absolute;left:80px;top:235px}
.contact .body{left:80px;top:254px;width:500px;font-size:13.5px;line-height:22.5px;color:var(--muted)}
.info{left:80px;display:flex;gap:14px;align-items:center}
.info .ico{width:34px;height:34px;background:#eef1f7;display:flex;align-items:center;justify-content:center}
.info b{display:block;font-size:12px;font-weight:600}
.info small{font-size:10px;color:var(--muted)}
.form{left:627px;top:83px;width:491px;height:482px;background:var(--paper);border:1px solid var(--line);padding:36px}
.form label{display:block;font-family:"Barlow Condensed",sans-serif;font-weight:700;font-size:10.5px;letter-spacing:1px;margin-bottom:9px}
.field{height:38px;background:var(--white);border:1px solid var(--line);font-size:11px;color:#9aa1ae;padding:0 14px;display:flex;align-items:center}
.grid2{display:flex;gap:18px}
.grid2>div{flex:1}
.group{margin-bottom:20px}
.form .area{height:92px;align-items:flex-start;padding-top:14px}
.form .btn{width:100%;height:44px;background:var(--navy);color:var(--white);font-size:11px}

/* footer */
.footer{height:366px;background:var(--navy-deep);color:#8f9bb5}
.footer .brand{left:80px;top:70px;position:absolute;font-size:20px}
.footer .about{left:80px;top:120px;width:260px;font-size:11.5px;line-height:20px}
.fcol{top:62px}
.fcol h4{font-family:"Barlow Condensed",sans-serif;font-weight:700;font-size:10.5px;letter-spacing:1.2px;color:var(--white);margin-bottom:18px}
.fcol a{display:flex;align-items:center;gap:8px;font-size:11.5px;color:#8f9bb5;text-decoration:none;height:26px}
.fbottom{left:80px;right:82px;top:296px;border-top:1px solid rgba(255,255,255,.1);padding-top:30px;display:flex;justify-content:space-between;font-size:10px;color:#5d6a88}
</style>
</head>
<body>

<header class="nav">
  <div class="brand"><i></i>Larkspur Vale</div>
  <nav class="nav-links">
    <a href="#services">SERVICES</a>
    <a href="#why">WHY US</a>
    <a href="#stories">TESTIMONIALS</a>
    <a href="#contact">CONTACT</a>
    <a class="btn btn-red" href="#contact">Free Consultation</a>
  </nav>
</header>

<section class="section hero">
  <div class="hero-photo" role="img" aria-label="Photo of a grey multi-storey suburban house with front steps and lawn"></div>
  <div class="hero-shade"></div>
  <div class="abs tag eyebrow">Ohio's Premier Property Management</div>
  <h1 class="abs head">A True Partner,<span>Not Just A Vendor.</span></h1>
  <p class="abs lede">Larkspur Vale Management LLC delivers strategic, data-driven property management across the Cleveland–Akron area — preserving your asset value while improving tenant experience.</p>
  <div class="abs ctas">
    <a class="btn btn-red" href="#contact">Get A Free Consultation
      <svg width="12" height="12" viewBox="0 0 12 12" fill="none" stroke="#fff" stroke-width="1.5"><path d="M1 6h9M7 3l3 3-3 3"/></svg></a>
    <a class="btn btn-ghost" href="#services">Our Services</a>
  </div>
  <div class="abs stats">
    <div class="stat"><b>4</b><small>Service Tiers</small></div>
    <div class="stat"><b>100%</b><small>Ohio Focused</small></div>
    <div class="stat"><b>$99+</b><small>Starting Price</small></div>
    <div class="stat"><b>24/7</b><small>Owner Support</small></div>
  </div>
</section>

<section class="section services" id="services">
  <div class="eyebrow">Service Plans</div>
  <h2 class="head center-title" style="top:122px">Strategic Property Management Solutions</h2>
  <div class="rule"></div>
  <p class="intro">Choose the tier that fits your portfolio. Every plan includes our data-driven approach<br>and commitment to asset preservation.</p>
  <div class="plans">
    <article class="plan">
      <div class="ico"><svg width="16" height="16" viewBox="0 0 16 16" fill="none" stroke="#1c3a6f" stroke-width="1.4"><path d="M2 7l6-5 6 5v7H2z"/><path d="M6 14V9h4v5"/></svg></div>
      <div class="price">$99<small>/mo</small></div>
      <h3>Basic</h3>
      <p>Essential property management for owners who want professional oversight with core services. Ideal for single-unit landlords entering the managed portfolio model.</p>
      <a class="btn" href="#contact">Get Started</a>
    </article>
    <article class="plan">
      <div class="ico"><svg width="16" height="16" viewBox="0 0 16 16" fill="none" stroke="#1c3a6f" stroke-width="1.4"><path d="M1 12l5-5 3 3 6-6M11 4h4v4"/></svg></div>
      <div class="price">$149<small>/mo</small></div>
      <h3>Intermediate</h3>
      <p>Expanded management with proactive maintenance coordination and enhanced reporting. Designed for owners with growing rental portfolios.</p>
      <a class="btn" href="#contact">Get Started</a>
    </article>
    <article class="plan featured">
      <span class="badge">MOST POPULAR</span>
      <div class="ico"><svg width="16" height="16" viewBox="0 0 16 16" fill="none" stroke="#fff" stroke-width="1.4"><path d="M8 1l6 2.5V8c0 3.5-3 6-6 7-3-1-6-3.5-6-7V3.5z"/></svg></div>
      <div class="price">$199<small>/mo</small></div>
      <h3>Advanced</h3>
      <p>Full-service management leveraging advanced analytics and proven operational frameworks to maximize occupancy and asset value.</p>
      <a class="btn" href="#contact">Get Started</a>
    </article>
    <article class="plan">
      <div class="ico"><svg width="16" height="16" viewBox="0 0 16 16" fill="none" stroke="#1c3a6f" stroke-width="1.3"><path d="M8 1.5l2 4.3 4.6.5-3.4 3.1 1 4.6L8 11.7 3.8 14l1-4.6L1.4 6.3 6 5.8z"/></svg></div>
      <div class="price">$249<small>/mo</small></div>
      <h3>Advanced+</h3>
      <p>Our premium tier — comprehensive strategic management combining data-driven insights, dedicated support, and long-term portfolio resilience planning.</p>
      <a class="btn" href="#contact">Get Started</a>
    </article>
  </div>
</section>

<section class="section why" id="why">
  <div class="ring" style="left:790px;top:-40px;width:520px;height:520px"></div>
  <div class="ring" style="left:-260px;top:360px;width:440px;height:440px"></div>
  <div class="abs eyebrow">Why Choose Us</div>
  <h2 class="abs head">Expertise Rooted In Asset<br>Preservation</h2>
  <div class="rule"></div>
  <p class="abs body">Larkspur Vale Management LLC combines advanced analytics with proven operational frameworks to protect your property value while improving tenant experience. Our decades of collective expertise across the Cleveland-Akron market means your investment is in hands that understand Ohio real estate deeply.</p>
  <ul class="abs checks">
    <li><svg width="13" height="13" viewBox="0 0 14 14" fill="none" stroke="#c8262c" stroke-width="1.4"><circle cx="7" cy="7" r="6"/><path d="M4 7l2 2 4-4"/></svg>Data-driven methods that protect and grow your asset value</li>
    <li><svg width="13" height="13" viewBox="0 0 14 14" fill="none" stroke="#c8262c" stroke-width="1.4"><circle cx="7" cy="7" r="6"/><path d="M4 7l2 2 4-4"/></svg>Advanced analytics combined with proven operational frameworks</li>
    <li><svg width="13" height="13" viewBox="0 0 14 14" fill="none" stroke="#c8262c" stroke-width="1.4"><circle cx="7" cy="7" r="6"/><path d="M4 7l2 2 4-4"/></svg>Proactive maintenance approach minimizes costly repairs</li>
    <li><svg width="13" height="13" viewBox="0 0 14 14" fill="none" stroke="#c8262c" stroke-width="1.4"><circle cx="7" cy="7" r="6"/><path d="M4 7l2 2 4-4"/></svg>Regulatory compliance expertise keeps you protected</li>
    <li><svg width="13" height="13" viewBox="0 0 14 14" fill="none" stroke="#c8262c" stroke-width="1.4"><circle cx="7" cy="7" r="6"/><path d="M4 7l2 2 4-4"/></svg>Cost efficiency focus improves your net operating income</li>
    <li><svg width="13" height="13" viewBox="0 0 14 14" fill="none" stroke="#c8262c" stroke-width="1.4"><circle cx="7" cy="7" r="6"/><path d="M4 7l2 2 4-4"/></svg>Long-term portfolio resilience built into every management plan</li>
    <li><svg width="13" height="13" viewBox="0 0 14 14" fill="none" stroke="#c8262c" stroke-width="1.4"><circle cx="7" cy="7" r="6"/><path d="M4 7l2 2 4-4"/></svg>Tailored proposals — no one-size-fits-all contracts</li>
  </ul>
  <a class="abs btn btn-red" href="#contact">Start The Conversation
    <svg width="10" height="10" viewBox="0 0 10 10" fill="none" stroke="#fff" stroke-width="1.5"><path d="M3 1l4 4-4 4"/></svg></a>
  <div class="abs frame"></div>
  <div class="abs why-photo" role="img" aria-label="Photo of a tan three-storey townhouse with a garage, surrounded by trees"></div>
  <div class="abs occ"><b>98%</b><small>Average Occupancy Rate</small></div>
</section>

<section class="section stories" id="stories">
  <div class="eyebrow">Client Stories</div>
  <h2 class="head center-title" style="top:118px">What Ohio Owners Say</h2>
  <div class="rule"></div>
  <div class="quotes">
    <article class="quote">
      <div class="stars">
        <svg width="74" height="12" viewBox="0 0 74 12" fill="#c8262c"><path id="s" d="M6 0l1.8 3.8 4.2.5-3.1 2.9.8 4.2L6 9.3 2.3 11.4l.8-4.2L0 4.3l4.2-.5z"/><use href="#s" x="15.5"/><use href="#s" x="31"/><use href="#s" x="46.5"/><use href="#s" x="62"/></svg>
      </div>
      <p>"Larkspur Vale Management lives up to their promise — a true partner. They handle everything professionally and the data-driven reports give me complete visibility into my investment."</p>
      <div class="who"><b>Property Owner</b><small>CLEVELAND, OH</small></div>
    </article>
    <article class="quote">
      <div class="stars"><svg width="74" height="12" viewBox="0 0 74 12" fill="#c8262c"><use href="#s"/><use href="#s" x="15.5"/><use href="#s" x="31"/><use href="#s" x="46.5"/><use href="#s" x="62"/></svg></div>
      <p>"The consultative approach made all the difference. They took time to understand my portfolio goals before recommending a plan. Highly professional team that actually knows the Northeast Ohio market."</p>
      <div class="who"><b>Portfolio Investor</b><small>AKRON, OH</small></div>
    </article>
    <article class="quote">
      <div class="stars"><svg width="74" height="12" viewBox="0 0 74 12" fill="#c8262c"><use href="#s"/><use href="#s" x="15.5"/><use href="#s" x="31"/><use href="#s" x="46.5"/><use href="#s" x="62"/></svg></div>
      <p>"Finally a property management company that treats your investment like an asset, not a number. The proactive maintenance approach alone has saved me thousands in repairs."</p>
      <div class="who"><b>Rental Property Owner</b><small>NORTHEAST OHIO</small></div>
    </article>
  </div>
</section>

<section class="section cta">
  <h2 class="head">Ready To Stop Managing And Start Earning?</h2>
  <p>Let our team handle the day-to-day so you can focus on what matters. Schedule a<br>free, no-obligation consultation today.</p>
  <div class="row">
    <a class="btn btn-red" href="#contact">Schedule Free Consultation</a>
    <a class="btn btn-ghost" href="#contact"><svg width="13" height="10" viewBox="0 0 13 10" fill="none" stroke="#fff" stroke-width="1.2"><rect x=".6" y=".6" width="11.8" height="8.8"/><path d="M.6.6l5.9 4.6L12.4.6"/></svg>Email Us</a>
  </div>
</section>

<section class="section contact" id="contact">
  <div class="abs eyebrow">Get In Touch</div>
  <h2 class="abs head">Let's Talk About Your<br>Property</h2>
  <div class="rule"></div>
  <p class="abs body">Whether you have one rental unit or a growing portfolio, we want to hear about your situation. Fill out the form and a member of our Ohio team will follow up within one business day.</p>
  <div class="abs info" style="top:353px">
    <div class="ico"><svg width="13" height="10" viewBox="0 0 13 10" fill="none" stroke="#1c3a6f" stroke-width="1.2"><rect x=".6" y=".6" width="11.8" height="8.8"/><path d="M.6.6l5.9 4.6L12.4.6"/></svg></div>
    <div><b>info@larkspurvalemanagement.com</b><small>We respond within 24 hours</small></div>
  </div>
  <div class="abs info" style="top:407px">
    <div class="ico"><svg width="11" height="14" viewBox="0 0 11 14" fill="none" stroke="#1c3a6f" stroke-width="1.2"><path d="M5.5 13S1 8.5 1 5.5a4.5 4.5 0 019 0C10 8.5 5.5 13 5.5 13z"/><circle cx="5.5" cy="5.5" r="1.6"/></svg></div>
    <div><b>Cleveland-Akron, Ohio</b><small>Serving Northeast Ohio</small></div>
  </div>
  <form class="abs form">
    <div class="grid2 group">
      <div><label>FULL NAME *</label><div class="field">John Smith</div></div>
      <div><label>PHONE NUMBER</label><div class="field">Your phone number</div></div>
    </div>
    <div class="group"><label>EMAIL ADDRESS *</label><div class="field">john@example.com</div></div>
    <div class="group"><label>NUMBER OF PROPERTIES</label><div class="field"></div></div>
    <div class="group"><label>TELL US ABOUT YOUR SITUATION</label><div class="field area">Location, property type, current challenges...</div></div>
    <a class="btn" href="#contact">Send My Request
      <svg width="12" height="12" viewBox="0 0 12 12" fill="none" stroke="#fff" stroke-width="1.5"><path d="M1 6h9M7 3l3 3-3 3"/></svg></a>
  </form>
</section>

<footer class="section footer">
  <div class="brand"><i></i>Larkspur Vale</div>
  <p class="abs about">Ohio's trusted full-service property management company. Protecting investments, building relationships.</p>
  <div class="abs fcol" style="left:438px">
    <h4>OUR SERVICES</h4>
    <a href="#services">Property Management</a>
    <a href="#services">Tenant Screening</a>
    <a href="#services">Maintenance Coordination</a>
    <a href="#services">Financial Reporting</a>
    <a href="#services">Leasing Services</a>
    <a href="#services">Eviction Assistance</a>
  </div>
  <div class="abs fcol" style="left:796px">
    <h4>CONTACT US</h4>
    <a href="#contact"><svg width="11" height="8" viewBox="0 0 13 10" fill="none" stroke="#8f9bb5" stroke-width="1.3"><rect x=".6" y=".6" width="11.8" height="8.8"/><path d="M.6.6l5.9 4.6L12.4.6"/></svg>info@larkspurvalemanagement.com</a>
    <a href="#contact"><svg width="9" height="12" viewBox="0 0 11 14" fill="none" stroke="#8f9bb5" stroke-width="1.3"><path d="M5.5 13S1 8.5 1 5.5a4.5 4.5 0 019 0C10 8.5 5.5 13 5.5 13z"/><circle cx="5.5" cy="5.5" r="1.6"/></svg>Cleveland-Akron, Ohio</a>
  </div>
  <div class="abs fbottom">
    <span>© 2026 Larkspur Vale Management. All rights reserved.</span>
    <span>Licensed Property Management · Ohio</span>
  </div>
</footer>

</body>
</html>
```